Membership card design for video game arena

I need a two sided design for membership cards for my customers. It needs to have instructions on how to book on one side, and a nice catchy design for the other.

Please pull logo and whatever you desire from the website www.vornik-play.com

Industry/Entity Type

Entertainment

Contact Information for Business Card

The front must say Vornik-Play with the address and whatever design you choose. The back must have the details below

Colors

Designer to choose colors to be used in the design.

Requirements
Must have
• Frontside
• Company name address and phone number
• Backside
• Booking Instructions
• www.Vornik-Play.com/book-now
• Click on General Admission and input information
• Use code Gatepass7 to gain access
• See you there!
Nice to have
• A nice design and whatever you find is pertinent
Should not have
• Useless info

```html
<!DOCTYPE html>
<html lang="en">
<head>
<meta charset="utf-8">
<title>Vornik-Play Membership Card</title>
<link href="https://fonts.googleapis.com/css2?family=Montserrat:ital,wght@0,400;0,500;0,700;1,700&family=Great+Vibes&display=swap" rel="stylesheet">
<style>
  :root {
    --page: #e8e4de;
    --violet: #7b3b8f;
    --indigo: #4a3f8c;
    --plum: #6a2f7e;
    --magenta: #a0408f;
    --white: #ffffff;
    --ink: #1c1c1c;
    --rose-light: #f3b8cf;
    --rose-deep: #c2306a;
    --silver-light: #f4f4f4;
    --silver-mid: #cfcfcf;
    --sans: "Montserrat", Arial, sans-serif;
    --script: "Great Vibes", cursive;
  }
  * { box-sizing: border-box; margin: 0; padding: 0; }
  html, body { width: 1200px; height: 1200px; overflow: hidden; }
  body { background: var(--page); position: relative; font-family: var(--sans); }

  .card {
    position: absolute;
    left: 160px;
    width: 880px;
    height: 530px;
    border-radius: 28px;
    overflow: hidden;
    color: var(--white);
    background:
      radial-gradient(ellipse 60% 55% at 50% 45%, rgba(160,64,143,0.35), transparent 70%),
      radial-gradient(ellipse 90% 80% at 50% 50%, var(--violet) 0%, var(--plum) 55%, var(--indigo) 100%);
    box-shadow: 0 14px 22px rgba(0,0,0,0.18);
  }
  .card--front { top: 32px; }
  .card--back { top: 602px; }

  .card__texture {
    position: absolute; inset: 0;
    background: linear-gradient(180deg, rgba(255,255,255,0.04) 0%, transparent 40%, rgba(180,70,150,0.18) 100%);
  }

  /* Front */
  .brand { position: absolute; display: flex; align-items: center; gap: 18px; }
  .brand__dot { width: 86px; height: 86px; border-radius: 50%; background: var(--white); flex: none; }
  .brand__name { font-weight: 700; color: var(--white); letter-spacing: 2px; text-transform: uppercase; line-height: 1; }
  .card--front .brand { left: 118px; top: 193px; }
  .card--front .brand__name { font-size: 64px; }

  .contact { position: absolute; left: 222px; top: 285px; font-size: 21px; font-weight: 400; letter-spacing: 0.6px; line-height: 34px; }

  /* Back */
  .card--back .brand { left: 0; right: 0; top: 88px; justify-content: center; }
  .card--back .brand__dot { width: 60px; height: 60px; }
  .card--back .brand__name { font-size: 48px; }

  .card-title {
    position: absolute; left: 0; right: 0; top: 196px; text-align: center;
    font-family: var(--script); font-size: 78px; line-height: 1;
    background: linear-gradient(180deg, var(--rose-light) 10%, var(--rose-deep) 90%);
    -webkit-background-clip: text; background-clip: text; color: transparent;
  }

  .booking-band {
    position: absolute; left: 0; right: 0; top: 346px; height: 38px;
    background: linear-gradient(90deg, var(--silver-light) 0%, var(--silver-mid) 25%, var(--silver-light) 50%, var(--silver-mid) 80%, var(--silver-light) 100%);
    color: var(--ink); font-size: 21px; font-weight: 500; letter-spacing: 1.5px;
    text-align: center; line-height: 38px; text-transform: uppercase;
  }

  .booking-steps { position: absolute; left: 0; right: 0; top: 392px; text-align: center; font-size: 16.5px; letter-spacing: 0.8px; line-height: 24px; }
  .booking-steps strong { font-weight: 700; font-style: italic; }
  .sign-off { position: absolute; left: 0; right: 0; top: 464px; text-align: center; font-family: var(--script); font-size: 30px; line-height: 1; }
</style>
</head>
<body>
  <section class="card card--front" aria-label="Membership card front">
    <div class="card__texture" role="img" aria-label="Soft purple speckled sparkle texture"></div>
    <div class="brand">
      <span class="brand__dot"></span>
      <span class="brand__name">Vornik-Play</span>
    </div>
    <p class="contact">2150 W Harlow St, Brinkton, FL 33911, USA<br>Phone: +1 555 014 2290</p>
  </section>

  <section class="card card--back" aria-label="Membership card back">
    <div class="card__texture" role="img" aria-label="Soft purple speckled sparkle texture"></div>
    <div class="brand">
      <span class="brand__dot"></span>
      <span class="brand__name">Vornik-Play</span>
    </div>
    <h1 class="card-title">Membership Card</h1>
    <h2 class="booking-band">Booking Instructions</h2>
    <p class="booking-steps">
      www.Vornik-Play.com/<strong>book-now</strong><br>
      Click on <strong>General Admission</strong> and input information<br>
      Use code <strong>Gatepass7</strong> to gain access
    </p>
    <p class="sign-off">See you there!</p>
  </section>
</body>
</html>
```